Brickline Rentals podcast postcard

I've launched a podcast about apartment investing, ownership and management which is newly up on orbix and wavlino. I want to create a postcard that I can mail to my client base to get them to subscribe

```html
<!DOCTYPE html>
<html lang="en">
<head>
<meta charset="utf-8">
<title>Brickline Rentals Podcast Postcard</title>
<link rel="stylesheet" href="https://fonts.googleapis.com/css2?family=Oswald:wght@500;600;700&family=Montserrat:wght@400;600&display=swap">
<style>
  :root {
    --page: #e9e9ec;
    --card: #ffffff;
    --lavender: #ebebf4;
    --purple: #3b3884;
    --purple-light: #4b479e;
    --orange: #f26a1b;
    --sky: #1e90d8;
    --navy: #2b2a86;
    --ink: #1d1d2a;
    --rule: #cfcfd6;
    --stamp: #cfcfcf;
    --pale-blue: #d7ecfa;
    --mid-blue: #79c6ef;
  }
  * { margin: 0; padding: 0; box-sizing: border-box; }
  html, body { width: 1200px; height: 900px; overflow: hidden; }
  body { background: var(--page); position: relative; font-family: "Montserrat", sans-serif; }

  .postcard {
    position: absolute;
    top: 265px;
    width: 555px;
    height: 370px;
    background: var(--card);
    box-shadow: 0 6px 18px rgba(0,0,0,0.15);
    overflow: hidden;
  }
  .postcard--back { left: 30px; }
  .postcard--front { left: 615px; }
  .postcard-shapes { position: absolute; inset: 0; }

  .brand-title { position: absolute; font-family: "Oswald", sans-serif; text-transform: uppercase; line-height: 0.95; }
  .brand-title .line-small { display: block; font-weight: 500; }
  .brand-title .line-large { display: block; font-weight: 600; }
  .tagline { position: absolute; font-family: "Oswald", sans-serif; font-weight: 700; color: var(--orange); text-transform: uppercase; white-space: nowrap; }

  /* back */
  .postcard--back .brand-title { left: 32px; top: 40px; color: #fff; }
  .postcard--back .line-small { font-size: 30px; }
  .postcard--back .line-large { font-size: 48px; }
  .postcard--back .tagline { left: 34px; top: 134px; font-size: 18px; }
  .back-body {
    position: absolute; left: 40px; top: 222px; width: 258px;
    font-size: 8.6px; line-height: 1.6; color: var(--ink); text-align: justify;
  }
  .back-contact {
    position: absolute; left: 246px; top: 322px;
    font-size: 9px; font-weight: 600; color: var(--ink);
  }
  .stamp-box { position: absolute; right: 26px; top: 14px; width: 62px; height: 60px; border: 3px solid var(--stamp); }
  .address-line { position: absolute; left: 340px; width: 192px; border-top: 1px dashed var(--rule); }

  /* front */
  .postcard--front .brand-title { left: 22px; top: 212px; }
  .postcard--front .line-small { font-size: 38px; color: var(--sky); }
  .postcard--front .line-large { font-size: 54px; color: var(--navy); }
  .postcard--front .tagline { left: 22px; top: 318px; font-size: 23px; }
</style>
</head>
<body>

  <section class="postcard postcard--back">
    <svg class="postcard-shapes" viewBox="0 0 555 370" width="555" height="370">
      <rect x="0" y="0" width="320" height="370" fill="var(--lavender)"/>
      <polygon points="0,150 0,260 120,190" fill="#ffffff"/>
      <polygon points="0,300 0,370 175,370" fill="#ffffff"/>
      <polygon points="0,0 320,0 320,128 165,205 0,140" fill="var(--purple)"/>
      <polygon points="150,0 270,0 170,110 90,60" fill="var(--purple-light)" opacity="0.55"/>
      <path d="M275 128 L275 70 Q275 45 300 45 L320 45 L320 112 Z" fill="var(--purple-light)" opacity="0.6"/>
      <polygon points="0,0 60,0 0,70" fill="var(--purple-light)" opacity="0.4"/>
    </svg>

    <h2 class="brand-title">
      <span class="line-small">Brickline</span>
      <span class="line-large">Rentals</span>
    </h2>
    <p class="tagline">Investing, owning, managing</p>

    <p class="back-body">The Brickline Rentals podcast is now live on orbix and wavlino. Each episode covers investing in, owning and managing apartments, with practical tips from people who run buildings every day. Subscribe today so you never miss a new episode, and share it with a fellow owner who could use the advice.</p>
    <p class="back-contact">Contact</p>

    <div class="stamp-box"></div>
    <div class="address-line" style="top:200px"></div>
    <div class="address-line" style="top:232px"></div>
    <div class="address-line" style="top:264px"></div>
    <div class="address-line" style="top:296px"></div>
  </section>

  <section class="postcard postcard--front">
    <svg class="postcard-shapes" viewBox="0 0 555 370" width="555" height="370">
      <defs>
        <linearGradient id="city-dusk" x1="0" y1="0" x2="0" y2="1">
          <stop offset="0" stop-color="#2f7de0"/>
          <stop offset="0.45" stop-color="#6fa6e6"/>
          <stop offset="0.75" stop-color="#2d3f73"/>
          <stop offset="1" stop-color="#1c2440"/>
        </linearGradient>
      </defs>
      <path role="img" aria-label="Photo of modern glass apartment buildings lit at dusk along a waterfront"
            d="M70 0 L555 0 L555 330 L430 330 Q410 330 395 320 L30 115 Q12 104 18 80 Q30 20 70 0 Z"
            fill="url(#city-dusk)"/>
      <polygon points="430,370 555,300 555,370" fill="var(--pale-blue)"/>
      <polygon points="330,370 400,370 490,320 440,322" fill="var(--mid-blue)"/>
    </svg>

    <h2 class="brand-title">
      <span class="line-small">Brickline</span>
      <span class="line-large">Rentals</span>
    </h2>
    <p class="tagline">Investing, owning, managing</p>
  </section>

</body>
</html>
```